New Company Website

Need a new website for my company Loxley Greenery.
Loxley Greenery offers four business lines: Interior Landscaping, Urbanscaping, Holiday Decorating, and Rental Plants.
Interior Landscaping is the interior installation and maintenance of live plants and flowers in corporate offices. Interiorscape contracts will be for a variety of terms from month to month to 3 years with differing price points in each option.
Urbanscaping refers to landscaping in the urban environment and is restricted in this definition to street side planters and medians, monument plantings and rooftop/balcony gardens.
Holiday Decorating is the Christmas/Hanukkah decorating during the winter season for corporate offices. The model for this business is to lease decorations for a period of 3 years.
Plant rentals is the short term rental of plants and live flowers (orchids, kalanchoe, etc) to event venues. The long term plan is to become the exclusive interior plant vendor for tradeshow organizations in the Tri-State area.

Target Market(s)

Office Managers, Building Managers, Event Coordinators

Industry/Entity Type

Landscaping

Requirements
Must have
• I love my logo. Please incorporate and use colors. Do not change logo.
Nice to have
• These are my competitors:
www.fernhollowdecor.com
www.qorvel.com

```html
<!DOCTYPE html>
<html lang="en">
<head>
<meta charset="utf-8">
<title>Loxley Greenery</title>
<link rel="stylesheet" href="https://fonts.googleapis.com/css2?family=Open+Sans:wght@400;600;700&family=Varela+Round&display=swap">
<style>
:root{
  --brand-blue:#1a6fb8;
  --brand-green:#5cbc47;
  --heading-green:#3b9a1e;
  --text-gray:#666;
  --nav-gray:#555;
  --link-blue:#2a74c0;
  --footer-dark:#1f1f1f;
  --footer-darker:#161616;
  --panel-dark:#2b2b2b;
  --footer-text:#cfcfcf;
  --footer-link:#5cbc47;
  --button-green:#2f8f3c;
  --white:#fff;
}
*{margin:0;padding:0;box-sizing:border-box}
html,body{width:738px;height:1200px;overflow:hidden;background:var(--white)}
body{position:relative;font-family:"Open Sans",Arial,sans-serif;color:var(--text-gray)}
.abs{position:absolute}
.top-bar{left:0;top:0;width:738px;height:3px;background:linear-gradient(90deg,var(--brand-blue) 50%,var(--brand-green) 50%)}
.brand{left:100px;top:30px;display:flex;align-items:center;gap:6px}
.brand-mark{width:14px;height:14px;background:var(--brand-green)}
.brand-name{font-size:13px;font-weight:700;color:var(--brand-blue)}
.social-dot{width:15px;height:15px;border-radius:50%;background:#666}
.call-label{left:546px;top:26px;font-size:6.5px;color:#777;letter-spacing:.2px}
.call-number{left:546px;top:33px;font-size:13px;font-weight:700;color:var(--brand-blue)}
.main-nav{top:61px;font-size:8px;font-weight:700;color:var(--nav-gray);letter-spacing:.8px}
.hero{left:100px;top:88px;width:537px;height:267px;background:linear-gradient(135deg,#d9d4cc 0%,#8f9a7d 35%,#5f8a3c 50%,#9a6a40 75%,#c08a57 100%)}

.service-card{width:262px;display:flex;flex-direction:column}
.service-title{font-size:11.5px;font-weight:700;color:var(--heading-green);letter-spacing:.9px;line-height:14px;height:19px}
.service-photo{width:262px;height:99px}
.service-text{margin-top:7px;font-size:5.9px;line-height:8.6px;color:var(--text-gray);letter-spacing:-.05px}
.read-more{margin-top:10px;font-size:4.6px;font-weight:700;color:var(--link-blue);text-decoration:underline;line-height:6px}

.testimonials{left:3px;top:763px;width:732px;height:132px;background:var(--brand-green)}
.testimonials-title{left:0;top:16px;width:732px;text-align:center;font-family:"Varela Round","Open Sans",sans-serif;font-size:17px;font-weight:400;color:#eaf7e4}
.testimonial{top:49px;display:flex;gap:6px}
.quote{width:116px;margin-top:7px;font-size:5.7px;line-height:9.3px;font-style:italic;color:var(--white)}
.client{width:60px;display:flex;flex-direction:column;align-items:center}
.avatar{width:40px;height:40px;border-radius:50%;border:2px solid #e9f5e4;background:linear-gradient(#b99a84,#8a6d5b)}
.client-name{margin-top:6px;font-size:7px;font-weight:600;color:#eaf7e4;line-height:10px}
.client-place{font-size:6px;font-weight:600;color:#2f8a2a;line-height:9px}

.footer{left:3px;top:895px;width:732px;height:263px;background:var(--footer-dark)}
.footer-brand{left:101px;top:977px;display:flex;align-items:center;gap:5px}
.footer-brand .brand-mark{background:#9a9a9a;width:12px;height:12px}
.footer-brand .brand-name{color:#a8a8a8;font-size:11px}
.footer-heading{font-size:10px;font-weight:400;color:var(--white);letter-spacing:.2px}
.footer-col{display:flex;flex-direction:column;gap:10px}
.footer-copy{font-size:5.8px;line-height:9.3px;color:var(--footer-text)}
.contact-list{display:flex;flex-direction:column;gap:6px;margin-top:2px}
.contact-row{display:flex;align-items:center;gap:9px;font-size:6px;color:var(--white)}
.contact-row svg{width:9px;flex:none}
.newsletter{left:498px;top:926px;width:138px;height:92px;background:var(--panel-dark)}
.newsletter-title{left:10px;top:10px;display:flex;align-items:center;gap:7px;font-size:5.8px;font-weight:600;color:var(--white);letter-spacing:.3px;white-space:nowrap}
.newsletter-rule{left:0;top:28px;width:138px;height:1px;background:#3a3a3a}
.email-field{left:9px;top:34px;width:119px;height:18px;background:#e8e8ee;font-size:7px;color:#666;padding:4px 7px;white-space:nowrap}
.subscribe{left:9px;top:61px;width:61px;height:18px;background:var(--button-green);color:var(--white);font-size:7px;text-align:center;line-height:18px}
.footer-rule{left:100px;top:1039px;width:537px;height:1px;background:#333}
.link-list{list-style:none;font-size:5.7px;line-height:11px;color:var(--footer-link)}
.link-list li{display:flex;align-items:center;gap:5px;white-space:nowrap}
.link-list li::before{content:"";border-left:3px solid #999;border-top:2.5px solid transparent;border-bottom:2.5px solid transparent}
.copyright-bar{left:3px;top:1158px;width:732px;height:42px;background:var(--footer-darker)}
.copyright{left:100px;top:1174px;font-size:6.3px;color:var(--footer-text)}
</style>
</head>
<body>
<div class="abs top-bar"></div>

<header>
  <div class="abs brand"><span class="brand-mark"></span><span class="brand-name">Loxley Greenery</span></div>
  <span class="abs social-dot" style="left:453px;top:30px"></span>
  <span class="abs social-dot" style="left:475px;top:30px"></span>
  <span class="abs social-dot" style="left:497px;top:30px"></span>
  <div class="abs call-label">&#9990; CALL US FOR CONSULATION</div>
  <div class="abs call-number">1800.555.0142</div>
  <nav>
    <span class="abs main-nav" style="left:383px">HOME</span>
    <span class="abs main-nav" style="left:450px">SERVICES</span>
    <span class="abs main-nav" style="left:529px">ABOUT</span>
    <span class="abs main-nav" style="left:590px">CONTACT US</span>
  </nav>
</header>

<div class="abs hero" role="img" aria-label="Open-plan modern interior with a raised planter of green plants on a concrete platform, wood floors and a bedroom area"></div>

<section>
  <article class="abs service-card" style="left:100px;top:385px">
    <h2 class="service-title">INTERIOR LANDSCAPING</h2>
    <div class="service-photo" style="background:linear-gradient(90deg,#c9c3b4,#e6e2d8 40%,#7f9a5a 85%,#556f3a)" role="img" aria-label="Bright office lounge with large windows and potted plants"></div>
    <p class="service-text">Interior Landscaping is the interior installation and maintenance of live plants and flowers in corporate offices. Interiorscape contracts will be for a variety of terms from month to month to 3 years with differing price points in each option.</p>
    <a class="read-more">READ MORE</a>
  </article>

  <article class="abs service-card" style="left:376px;top:385px">
    <h2 class="service-title">PLANT RENTALS</h2>
    <div class="service-photo" style="background:linear-gradient(90deg,#8a7a68,#b9b1a6 35%,#cfc9c0 70%,#6f8f3a)" role="img" aria-label="Minimal room with a large leafy potted plant and modern chairs"></div>
    <p class="service-text">Plant rentals is the short term rental of plants and live flowers (orchids, kalanchoe, etc) to event venues. The long term plan is to become the exclusive interior plant vendor for trade-show organizations in the Tri-State area.</p>
    <a class="read-more">READ MORE</a>
  </article>

  <article class="abs service-card" style="left:100px;top:571px">
    <h2 class="service-title">HOLIDAY DECORATING</h2>
    <div class="service-photo" style="background:linear-gradient(90deg,#e9e7e2,#d8d2c4 45%,#4f6b36 75%,#e8e4dc)" role="img" aria-label="Fireplace mantel with garland, stockings and a decorated holiday tree"></div>
    <p class="service-text">Holiday Decorating is the Christmas/Hanukkah decorating during the winter season for corporate offices. The model for this business is to lease decorations for a period of 3 years.</p>
    <a class="read-more">READ MORE</a>
  </article>

  <article class="abs service-card" style="left:376px;top:571px">
    <h2 class="service-title">URBANSCAPING</h2>
    <div class="service-photo" style="background:linear-gradient(160deg,#5e7f3e,#a9a397 45%,#4f7a2e 80%,#c7c0b3)" role="img" aria-label="Terraced stone garden with shrubs and steps"></div>
    <p class="service-text">Urbanscaping refers to landscaping in the urban environment and is restricted in this definition to street side planters and medians, monument plantings and rooftop/balcony gardens.</p>
    <a class="read-more">READ MORE</a>
  </article>
</section>

<section class="abs testimonials">
  <h2 class="abs testimonials-title">Client Testimonials</h2>
  <div class="abs testimonial" style="left:172px">
    <p class="quote">"Lorem ipsum dolor sit amet, consectetur adipisicing elit, sed do eiusmod tempor incididunt ut labore et dolore magna aliqua.</p>
    <div class="client">
      <div class="avatar" role="img" aria-label="Client portrait"></div>
      <div class="client-name">Marcus Hale</div>
      <div class="client-place">San Antonio, TX</div>
    </div>
  </div>
  <div class="abs testimonial" style="left:380px">
    <p class="quote">"Lorem ipsum dolor sit amet, consectetur adipisicing elit, sed do eiusmod tempor incididunt ut labore et dolore magna aliqua.</p>
    <div class="client">
      <div class="avatar" role="img" aria-label="Client portrait"></div>
      <div class="client-name">Dana Brill</div>
      <div class="client-place">San Antonio, TX</div>
    </div>
  </div>
</section>

<footer>
  <div class="abs footer"></div>
  <div class="abs footer-brand"><span class="brand-mark"></span><span class="brand-name">Loxley Greenery</span></div>

  <div class="abs footer-col" style="left:222px;top:926px;width:100px">
    <h3 class="footer-heading">ABOUT US</h3>
    <p class="footer-copy">There are many variations of pas-sages of Lorem Ipsum available.</p>
    <p class="footer-copy">There are many variations of pas-sages of Lorem Ipsum available, but the majority have suffered alteration.</p>
  </div>

  <div class="abs footer-col" style="left:361px;top:926px;width:112px">
    <h3 class="footer-heading">CONTACT</h3>
    <p class="footer-copy">There are many variations of passag-es of Lorem Ipsum available, but the majority have suffered alteration.</p>
    <div class="contact-list">
      <div class="contact-row">
        <svg height="9" viewBox="0 0 9 9"><path d="M4.5 0A3.3 3.3 0 0 0 1.2 3.3C1.2 5.8 4.5 9 4.5 9S7.8 5.8 7.8 3.3A3.3 3.3 0 0 0 4.5 0z" fill="#aaa"/><circle cx="4.5" cy="3.3" r="1.2" fill="#1f1f1f"/></svg>
        <span>New Delhi</span></div>
      <div class="contact-row">
        <svg height="7" viewBox="0 0 9 7"><rect width="9" height="7" fill="#aaa"/><path d="M0 0l4.5 3.8L9 0" stroke="#1f1f1f" fill="none"/></svg>
        <span>hello@loxleygreenery.com</span></div>
      <div class="contact-row">
        <svg height="8" viewBox="0 0 9 8"><path d="M1.6 0l1.4 1.9-.8 1.1a5 5 0 0 0 2.8 2.8l1.1-.8L8 6.4 6.9 8C3 7.6.4 5 0 1.1z" fill="#aaa"/></svg>
        <span>890-55501-42277</span></div>
    </div>
  </div>

  <div class="abs newsletter">
    <div class="abs newsletter-title">
      <svg width="10" height="7" viewBox="0 0 10 7"><rect width="10" height="7" fill="#fff"/><path d="M0 0l5 4 5-4" stroke="#2b2b2b" fill="none"/></svg>
      <span>SUBSCRIBE TO OUR NEWSLETTER</span></div>
    <div class="abs newsletter-rule"></div>
    <div class="abs email-field">Enter your email address</div>
    <div class="abs subscribe">SUBSCRIBE</div>
  </div>

  <div class="abs footer-rule"></div>

  <h3 class="abs footer-heading" style="left:101px;top:1064px">NAVIGATION</h3>
  <ul class="abs link-list" style="left:101px;top:1082px"><li>Home</li><li>About Us</li><li>Services</li><li>Contact Us</li></ul>

  <h3 class="abs footer-heading" style="left:239px;top:1064px">SERVICES</h3>
  <ul class="abs link-list" style="left:239px;top:1082px"><li>Interior Landscaping</li><li>Urbanscaping</li><li>Holiday Decorating</li><li>Rental Plants</li></ul>

  <h3 class="abs footer-heading" style="left:361px;top:1064px">SITE LINKS</h3>
  <ul class="abs link-list" style="left:361px;top:1082px"><li>Business Inquiries</li><li>Feedback</li><li>Privacy Policy</li><li>Site Map</li></ul>

  <h3 class="abs footer-heading" style="left:501px;top:1064px">SOCIAL</h3>
  <span class="abs social-dot" style="left:500px;top:1083px;background:#777"></span>
  <span class="abs social-dot" style="left:522px;top:1083px;background:#777"></span>
  <span class="abs social-dot" style="left:544px;top:1083px;background:#777"></span>

  <div class="abs copyright-bar"></div>
  <p class="abs copyright">Copyright 2013 © Loxley Greenery - All Rights Reserved</p>
</footer>
</body>
</html>
```